Counselling business requires poster

I require a poster to promote my counselling and coaching business I will be placing these in doctors surgery's and clinics etc.
This business is centred around helping people work through emotional issues. We provided one on one sessions which help enhance peoples lives by assisting them in overcoming their fears, obsessions, insecurities etc.

We offer support in a broad range of areas:

- Eating disorders & weight managment
- Depression
- Marriage and relationship issues
- Anxiety
- Victims of physical, verbal and/or social abuse

We want our poster to be representative of the positive, warm and welcoming atmosphere we provide.

Our motto, 'One step at a time', is symbolic of our approach and how we help our clients to tackle their problems bit by bit.

The flyer I have uploaded is just some information on what we offer

Thankyou for your designs I am taking them into consideration and will inform you of any decision.

Weight

```html
<!DOCTYPE html>
<html lang="en">
<head>
<meta charset="utf-8">
<title>Pathways Counselling – One Step at a Time</title>
<link rel="stylesheet" href="https://fonts.googleapis.com/css2?family=Montserrat:wght@400;800;900&family=Marcellus&display=swap">
<style>
  :root {
    --navy-deep: #0b1524;
    --navy: #16243a;
    --slate: #2c3b52;
    --green: #3db54a;
    --orange: #f7941d;
    --sky: #4cb6d2;
    --white: #ffffff;
  }
  * { margin: 0; padding: 0; box-sizing: border-box; }
  html, body {
    width: 849px;
    height: 1200px;
    overflow: hidden;
    background: var(--navy-deep);
  }
  .poster {
    position: relative;
    width: 849px;
    height: 1200px;
    overflow: hidden;
    font-family: "Montserrat", Arial, sans-serif;
    color: var(--white);
    text-align: center;
  }
  .backdrop {
    position: absolute;
    inset: 0;
  }
  .line {
    position: absolute;
    left: 0;
    width: 100%;
    line-height: 1;
    white-space: nowrap;
  }
  .headline {
    color: var(--green);
    font-weight: 900;
    font-size: 62px;
    letter-spacing: 0.5px;
  }
  .headline--small { font-size: 50px; }
  .concerns {
    font-weight: 800;
    font-size: 24px;
    letter-spacing: 0.5px;
  }
  .counsellor-name {
    font-family: "Marcellus", Georgia, serif;
    color: var(--orange);
    font-size: 54px;
    letter-spacing: 1px;
  }
  .practice {
    font-weight: 800;
    font-size: 46px;
    letter-spacing: 0.5px;
  }
  .helps {
    color: var(--green);
    font-weight: 900;
    font-size: 44px;
  }
  .promise {
    font-weight: 800;
    font-size: 25px;
    letter-spacing: 0.3px;
  }
  .motto {
    color: var(--green);
    font-style: italic;
  }
  .contact-label {
    color: var(--orange);
    font-weight: 900;
    font-size: 32px;
  }
  .brand-name {
    color: var(--sky);
    font-weight: 800;
    font-size: 72px;
    letter-spacing: 1px;
  }
  .brand-dot {
    display: inline-block;
    width: 46px;
    height: 46px;
    border-radius: 50%;
    background: var(--orange);
    vertical-align: middle;
    margin-right: 14px;
    position: relative;
    top: -6px;
  }
  .brand-tagline {
    font-weight: 400;
    font-size: 21px;
    letter-spacing: 5px;
  }
  .contact-details {
    position: absolute;
    left: 266px;
    top: 1102px;
    text-align: left;
    font-size: 20px;
    line-height: 27px;
  }
  .contact-details .key { color: var(--sky); margin-right: 4px; }
</style>
</head>
<body>
<main class="poster">
  <svg class="backdrop" width="849" height="1200" viewBox="0 0 849 1200" role="img" aria-label="Dark blue staircase rising diagonally across the poster">
    <defs>
      <linearGradient id="stair-tone" x1="0" y1="1" x2="1" y2="0">
        <stop offset="0" stop-color="#2c3b52"/>
        <stop offset="0.45" stop-color="#16243a"/>
        <stop offset="1" stop-color="#0b1524"/>
      </linearGradient>
    </defs>
    <rect width="849" height="1200" fill="url(#stair-tone)"/>
  </svg>

  <h1>
    <span class="line headline" style="top:50px">DON’T READ FURTHER</span>
    <span class="line headline" style="top:123px">IF YOU DON’T</span>
    <span class="line headline headline--small" style="top:198px">HAVE</span>
  </h1>

  <ul class="concerns-list">
    <li class="line concerns" style="top:268px">PROBLEMS WITH INTIMATE RELATIONSHIP</li>
    <li class="line concerns" style="top:308px">DEPRESSION OR ANXIETY</li>
    <li class="line concerns" style="top:348px">EATING DISORDERS</li>
    <li class="line concerns" style="top:389px">STRUGGLING WITH GRIEF</li>
    <li class="line concerns" style="top:428px">SELF ESTEEM ISSUES</li>
    <li class="line concerns" style="top:466px">WEIGHT LOSS MANAGEMENT</li>
    <li class="line concerns" style="top:506px">ABUSIVE RELATIONSHIPS</li>
  </ul>

  <p class="line counsellor-name" style="top:563px">DANA WHITMORE</p>
  <p class="line practice" style="top:624px">AT PATHWAYS</p>
  <p class="line practice" style="top:677px">COUNSELLING</p>
  <p class="line helps" style="top:733px">HELPS!</p>

  <p class="line promise" style="top:796px">YOU UNCOVER YOUR TRUE POTENTIAL AND</p>
  <p class="line promise" style="top:827px">LEAD A LIFE THAT IS WORTH CELEBRATING</p>
  <p class="line promise" style="top:858px">BY TAKING <span class="motto">ONE STEP AT A TIME</span></p>

  <p class="line contact-label" style="top:930px">CONTACT</p>
  <p class="line brand-name" style="top:980px"><span class="brand-dot"></span>PATHWAYS</p>
  <p class="line brand-tagline" style="top:1068px">PATHWAYS COUNSELLING</p>

  <address class="contact-details" style="font-style:normal">
    <div><span class="key">P</span>0400 555 128</div>
    <div><span class="key">E</span>pathwayscounselling@mail.com</div>
  </address>
</main>
</body>
</html>
```